Marlow Ridgeway a PlateWork Fabricator! Pressure Vessels, Stainless Vessels, Steel Fabricator!

Update and modernize the www.marlowridgeway.example website. Basically throwing away the old site and coming back with a new feel, new look, but some of the same content. One of our other companies is www.keltonbuilders.example and if you view that site you will get a idea of how we would like the site to feel. Below are the MR logos and the colors are #231F20 and #6D0B17 and the font is Ethnocentric Rg.

Target Market(s)

Steel Fabrication, Platework, Vessel Fabrication,

Industry/Entity Type

Steel

Coding

Coded - Design and coding required

Number of Pages Required

5+ page

Font styles to use
Other font styles liked:
• Ethnocentric Rg

Requirements
Must have
• Industry feel... site must flow and color scheme and font be consistent.

```html
<!DOCTYPE html>
<html lang="en">
<head>
<meta charset="utf-8">
<title>Marlow Ridgeway — Quality Fabrication</title>
<link rel="stylesheet" href="https://fonts.googleapis.com/css2?family=Open+Sans:wght@400;600;700;800&display=swap">
<style>
:root{
  --ink:#231f20;
  --brand:#6d0b17;
  --brand-bright:#8a1223;
  --nav:#7a0f1e;
  --paper:#ffffff;
  --mist:#e7e7e7;
  --footer:#2a2627;
  --footer-deep:#1f1c1d;
  --muted:#bdb8b9;
  --stage:#3a3a3a;
}
*{box-sizing:border-box;margin:0;padding:0}
html,body{width:719px;height:1200px;overflow:hidden;background:var(--stage)}
body{font-family:"Open Sans",Arial,sans-serif;color:var(--ink)}
.page{position:absolute;left:128px;top:0;width:540px;height:1400px;transform:scale(0.857);transform-origin:top left;background:var(--paper);overflow:hidden}
.abs{position:absolute}
.btn{position:absolute;display:flex;align-items:center;justify-content:center;border-radius:12px;font-size:7.5px;font-weight:600;color:#fff;text-transform:uppercase;letter-spacing:.2px}
.btn--brand{background:var(--brand-bright)}
.btn--dark{background:var(--ink)}
.btn--outline{background:rgba(255,255,255,.15);border:1px solid rgba(255,255,255,.25)}
.eyebrow{font-size:6.5px;letter-spacing:1.4px;font-weight:600;text-transform:uppercase}
.heading{font-weight:800;font-size:13.5px;text-transform:uppercase;letter-spacing:.2px}
.accent{color:var(--brand-bright)}
.copy{font-size:8.6px;line-height:1.28}

/* header */
.brand{position:absolute;left:16px;top:10px;display:flex;align-items:center;gap:6px}
.brand__mark{width:44px;height:44px;border-radius:50%;border:4px solid var(--ink)}
.brand__name{font-weight:800;font-size:15px;line-height:1;color:var(--ink);text-transform:uppercase}
.header__phone{left:333px;top:27px;font-size:10px;display:flex;align-items:center;gap:9px}
.nav{left:0;top:65px;width:540px;height:29px;background:var(--nav);display:flex;align-items:center;padding-left:20px;gap:15px}
.nav a{color:#fff;font-size:7.5px;font-weight:700;text-decoration:none;text-transform:uppercase}

/* hero */
.hero{left:0;top:94px;width:540px;height:234px;background:radial-gradient(ellipse at 30% 80%,#e0a34a 0%,#8a5a2a 25%,#3c3634 55%,#6d6a68 100%)}
.hero__panel{left:115px;top:155px;width:308px;height:112px;background:rgba(255,255,255,.86);border-radius:5px;text-align:center}
.hero__title{position:absolute;top:26px;width:100%;font-weight:800;font-size:10px;line-height:1.25;text-transform:uppercase}
.hero__select{left:42px;top:60px;width:132px;height:23px;border:1px solid #aaa;background:#fff;font-size:7.5px;display:flex;align-items:center;padding-left:10px}
.hero__btn{left:177px;top:60px;width:91px;height:23px;border-radius:2px;background:var(--brand-bright);color:#fff;font-size:8.5px;font-weight:600;display:flex;align-items:center;justify-content:center;text-transform:uppercase}

/* footer */
.footer{left:0;top:1113px;width:540px;height:227px;background:var(--footer)}
.footer__bar{left:0;top:1340px;width:540px;height:60px;background:var(--footer-deep)}
.footer-heading{position:absolute;font-size:7.5px;font-weight:600;color:#fff;text-transform:uppercase;line-height:1;white-space:nowrap}
.footer-small{position:absolute;font-size:6.6px;color:#ddd;line-height:1.3}
.footer-line{position:absolute;font-size:6.6px;color:#ddd;line-height:1;display:flex;gap:5px;align-items:center;white-space:nowrap}
.social{width:18px;height:18px;border:1.5px solid #fff;border-radius:50%}

/* form */
.field{position:absolute;border:1px solid rgba(255,255,255,.45);font-size:7.5px;color:#fff;padding:8px 12px}
</style>
</head>
<body>
<main class="page">

  <header>
    <div class="brand"><span class="brand__mark"></span><span class="brand__name">Marlow<br>Ridgeway</span></div>
    <div class="abs header__phone">
      <svg width="10" height="10" viewBox="0 0 24 24"><path fill="#8a1223" d="M6.6 10.8a15 15 0 006.6 6.6l2.2-2.2c.3-.3.7-.4 1-.2 1.1.4 2.3.6 3.6.6.6 0 1 .4 1 1V20c0 .6-.4 1-1 1A17 17 0 013 4c0-.6.4-1 1-1h3.5c.6 0 1 .4 1 1 0 1.3.2 2.5.6 3.6.1.3 0 .7-.2 1z"/></svg>
      555.014.2270
    </div>
    <div class="btn btn--brand" style="left:428px;top:22px;width:84px;height:21px;font-size:6.5px">Request a Quote</div>
    <nav class="abs nav">
      <a>Home</a><a>About</a><a>Products</a><a>Services Who</a><a>We Serve</a><a>Resources</a><a>Contact</a>
    </nav>
  </header>

  <section>
    <div class="abs hero" role="img" aria-label="Photo of a worker grinding steel with sparks flying"></div>
    <div class="abs hero__panel">
      <div class="hero__title">Your vision, our custom<br><span class="accent">Quality fabrication services</span></div>
      <div class="abs hero__select">Select A Product</div>
      <div class="abs hero__btn">View Product</div>
    </div>
  </section>

  <section>
    <svg class="abs" style="left:36px;top:372px" width="130" height="140" viewBox="0 0 130 140"><path d="M70 8 A62 62 0 0 0 70 132" fill="none" stroke="#6d0b17" stroke-width="9"/><path d="M32 118 A62 62 0 0 0 118 118" fill="none" stroke="#231f20" stroke-width="7"/></svg>
    <div class="abs" role="img" aria-label="Bundle of polished stainless steel pipes" style="left:50px;top:362px;width:165px;height:145px;border-radius:50%;background:radial-gradient(circle at 45% 40%,#f2f2f2,#9a9a9a 55%,#4a4a4a)"></div>
    <div class="abs eyebrow accent" style="left:236px;top:366px">Quality drives fabrication</div>
    <div class="abs heading" style="left:236px;top:380px">Quality assurance <span class="accent">guaranteed</span></div>
    <p class="abs copy" style="left:236px;top:408px;width:268px;color:#444">As experienced steel fabricators, we anticipate your needs and requirements from vision to production to delivery. Your steel fabrication products are manufactured by proven business processes and some of the industry's top experts.</p>
    <div class="btn btn--brand" style="left:236px;top:468px;width:76px;height:20px">Products</div>
    <div class="btn btn--dark" style="left:319px;top:468px;width:76px;height:20px">Services</div>
  </section>

  <section>
    <div class="abs" style="left:0;top:563px;width:540px;height:237px;background:linear-gradient(90deg,var(--brand-bright),var(--brand))"></div>
    <div class="abs eyebrow" style="left:38px;top:603px;color:#fff">Built to specifications large or small</div>
    <div class="abs heading" style="left:38px;top:616px;color:#fff"><span style="color:#231f20">Quality drives</span> fabrication</div>
    <p class="abs copy" style="left:38px;top:645px;width:240px;color:#fff">We deliver fabrication solutions from small scale projects to our specialized oversized and overweight fabrication, processing, and handling capabilities. Steel fabricators proudly serving the power generation, water treatment, waste treatment, agriculture, chemical, food processing, mining, oil &amp; gas and heavy industry project sectors for nearly 40 years.</p>
    <div class="btn btn--outline" style="left:38px;top:745px;width:93px;height:20px">Who we serve</div>
    <svg class="abs" style="left:292px;top:560px" width="240" height="240" viewBox="0 0 240 240"><circle cx="118" cy="115" r="112" fill="none" stroke="#231f20" stroke-width="10"/></svg>
    <div class="abs" role="img" aria-label="Black and white photo of a welder at work" style="left:314px;top:585px;width:196px;height:196px;border-radius:50%;background:radial-gradient(circle at 60% 70%,#ffffff,#9a9a9a 35%,#2a2a2a 80%)"></div>
  </section>

  <section>
    <div class="abs" style="left:0;top:800px;width:540px;height:313px;background:var(--mist)"></div>
    <div class="abs" role="img" aria-label="Faded photo of industrial storage tanks" style="left:0;top:970px;width:540px;height:143px;background:linear-gradient(180deg,rgba(231,231,231,0),#cfcfcf)"></div>
    <div class="abs eyebrow" style="left:0;top:827px;width:540px;text-align:center">Because our clients matter</div>
    <div class="abs heading" style="left:0;top:840px;width:540px;text-align:center;line-height:1.3">We may not be superheroes<br>but our <span class="accent">customers think we are.</span></div>
    <p class="abs copy" style="left:52px;top:880px;width:436px;text-align:center;color:#333">We will keep Marlow-Ridgeway steel fabricators on our bidding list for vessels, tanks and stacks. Our catch tank constructed by them was of excellent workmanship and the exterior and interior met all of our expectations. We were impressed with the knowledgeable sales and engineering staff as well as their facilities. They worked well from the calculations for the foundation to the final tank design.</p>
    <div class="btn btn--brand" style="left:190px;top:939px;width:74px;height:20px">Case Studies</div>
    <div class="btn btn--dark" style="left:273px;top:939px;width:76px;height:20px">Our Client</div>
  </section>

  <footer>
    <div class="abs footer"></div>
    <div class="abs" style="left:80px;top:974px;width:379px;height:223px;background:rgba(138,18,35,.94)"></div>
    <div class="abs eyebrow" style="left:80px;top:990px;width:379px;text-align:center;color:#fff">Start your project</div>
    <div class="abs heading" style="left:80px;top:1001px;width:379px;text-align:center;color:#fff">Request a quote</div>
    <div class="field" style="left:123px;top:1030px;width:144px;height:22px;padding-top:6px">First Name</div>
    <div class="field" style="left:272px;top:1030px;width:144px;height:22px;padding-top:6px">Company Name</div>
    <div class="field" style="left:123px;top:1058px;width:144px;height:22px;padding-top:6px">Phone Number</div>
    <div class="field" style="left:272px;top:1058px;width:144px;height:22px;padding-top:6px">Email</div>
    <div class="field" style="left:123px;top:1087px;width:293px;height:48px">Describe your project</div>
    <div class="abs" style="left:123px;top:1144px;width:112px;height:24px;background:#fff;color:var(--brand-bright);font-size:7.5px;font-weight:600;display:flex;align-items:center;justify-content:center">SUBMIT YOUR QUOTES</div>

    <div class="brand" style="left:42px;top:1220px"><span class="brand__mark" style="width:38px;height:38px;border-color:#fff"></span><span class="brand__name" style="color:#fff;font-size:13px">Marlow<br>Ridgeway</span></div>
    <p class="footer-small" style="left:38px;top:1271px;width:190px">Established in 1976, Marlow-Ridgeway is a privately-owned corporation that specializes in ASME custom steel fabrication of large steel and stainless-steel industrial process components.</p>
    <div class="footer-small" style="left:38px;top:1313px;color:var(--muted)">Read More</div>

    <h4 class="footer-heading" style="left:273px;top:1218px">Our Location</h4>
    <p class="footer-small" style="left:273px;top:1243px;width:150px">1180 Foundry Lane, Unit 4<br>Cedar Bend, FL 30417</p>
    <div class="footer-line" style="left:273px;top:1270px"><svg width="7" height="7" viewBox="0 0 24 24"><path fill="#fff" d="M6.6 10.8a15 15 0 006.6 6.6l2.2-2.2c.3-.3.7-.4 1-.2 1.1.4 2.3.6 3.6.6.6 0 1 .4 1 1V20c0 .6-.4 1-1 1A17 17 0 013 4c0-.6.4-1 1-1h3.5c.6 0 1 .4 1 1 0 1.3.2 2.5.6 3.6.1.3 0 .7-.2 1z"/></svg>555-014-2270</div>
    <div class="footer-line" style="left:273px;top:1288px"><svg width="7" height="7" viewBox="0 0 10 10"><rect x="1" y="3" width="8" height="5" fill="#fff"/><rect x="3" y="1" width="4" height="2" fill="#fff"/></svg>555-014-2271</div>
    <div class="footer-line" style="left:273px;top:1306px"><svg width="7" height="6" viewBox="0 0 10 8"><rect width="10" height="8" fill="#fff"/><path d="M0 0l5 4 5-4" stroke="#2a2627" fill="none"/></svg>info@marlowridgeway.example</div>

    <h4 class="footer-heading" style="left:426px;top:1218px">Connect with us</h4>
    <span class="abs social" style="left:426px;top:1237px"></span>
    <span class="abs social" style="left:455px;top:1237px"></span>
    <span class="abs social" style="left:483px;top:1237px"></span>

    <div class="abs footer__bar"></div>
    <div class="abs" style="left:40px;top:1366px;font-size:7.2px;color:#fff">© 2018 MARLOW-RIDGEWAY. ALL RIGHTS RESERVED.</div>
    <div class="btn btn--brand" style="left:427px;top:1361px;width:78px;height:19px;border-radius:10px">Start Today</div>
  </footer>

</main>
</body>
</html>
```